A Gallery type Web design

We are developing a Wordpress based website for a client that does design construction projects. E.g. Pools, Lobbies, Toilets, etc. The website will mainly be to showcase their past projects and the collections they have.
No programming required, we just need the designs!
A sample of what the client is looking for:
http://velmora.it/
Pages to include:
• Home – A nice slider design to showcase selected photos
• Main Category Template
• Sub Category Template
• About us
• Contact us
Example of their Main Categories and their Sub Categories:
Collections - Granite
- Marble
- Sculpture
Projects - Private
- Public
- Commercial
- Overseas
Installation - Vanity tops
- Hall areas
- Toilets
The Main Category is to show a sample and link the user to the respective Sub Categories. The Sub Categories are to showcase all the photos they have from the category. Please leave a little space to add some text or caption for the photo.
Designs need to be mobile responsive!
I've attached their logo and some sample photos to use for mock ups. Let me know if you have any questions!

```html
<!DOCTYPE html>
<html lang="en">
<head>
<meta charset="utf-8">
<title>Petra Grove – Home</title>
<link href="https://fonts.googleapis.com/css2?family=Oswald:wght@400;500&family=Open+Sans:wght@400;600;700&display=swap" rel="stylesheet">
<style>
  :root {
    --header-dark: #2a2a2a;
    --brand-red: #c8171d;
    --nav-red: #b7151a;
    --text-dark: #333333;
    --text-muted: #6a6a6a;
    --section-grey: #ececec;
    --footer-dark: #262626;
    --footer-line: #3d3d3d;
    --white: #ffffff;
  }
  * { box-sizing: border-box; margin: 0; padding: 0; }
  html, body { width: 896px; height: 1200px; overflow: hidden; }
  body { font-family: "Open Sans", Arial, sans-serif; color: var(--text-dark); background: var(--white); }

  .site-header {
    height: 104px; background: var(--header-dark);
    display: flex; align-items: center; justify-content: space-between; padding: 0 60px 0 34px;
  }
  .brand { display: flex; align-items: center; gap: 10px; }
  .brand-square { width: 24px; height: 24px; background: var(--brand-red); }
  .brand-name { font-family: "Oswald", sans-serif; font-weight: 500; font-size: 28px; color: var(--white); letter-spacing: 1px; }
  .call-now { font-size: 23px; color: var(--white); }
  .call-now .phone { color: var(--brand-red); }

  .main-nav { height: 20px; background: var(--nav-red); display: flex; align-items: center; padding-left: 60px; }
  .main-nav a { color: var(--white); text-decoration: none; font-size: 11px; padding: 0 24px; border-right: 1px solid rgba(255,255,255,.4); line-height: 12px; }
  .main-nav a:last-child { border-right: none; }

  .hero { position: relative; height: 432px; display: flex; }
  .hero-panel { height: 100%; }
  .hero-panel.lounge {
    width: 360px;
    background:
      linear-gradient(180deg, rgba(255,255,255,.55) 0%, rgba(255,255,255,0) 35%),
      linear-gradient(160deg, #e9e6e0 0%, #9c958b 35%, #3b3531 65%, #1e1b19 100%);
  }
  .hero-panel.fireplace {
    width: 252px;
    background:
      radial-gradient(ellipse 70px 50px at 50% 58%, #f0a040 0%, #b4541c 45%, rgba(40,30,25,0) 100%),
      linear-gradient(180deg, #8e8a86 0%, #b3aea8 40%, #77716b 70%, #5a4d3f 100%);
  }
  .hero-panel.bathroom {
    flex: 1;
    background:
      linear-gradient(90deg, rgba(0,0,0,.25) 0%, rgba(0,0,0,0) 20%),
      linear-gradient(170deg, #f4f2ef 0%, #cfcac3 45%, #8c8780 75%, #5e5a55 100%);
  }
  .hero-labels {
    position: absolute; left: 0; right: 0; bottom: 0; height: 36px;
    background: rgba(20,20,20,.72); display: flex;
  }
  .hero-labels span {
    flex: 1; text-align: center; color: var(--white);
    font-size: 21px; line-height: 36px; letter-spacing: 1px;
  }

  .welcome { height: 234px; text-align: center; padding: 24px 92px 0; }
  .welcome h1 { font-family: "Oswald", sans-serif; font-weight: 400; font-size: 27px; color: var(--brand-red); }
  .welcome h2 { font-size: 13px; font-weight: 700; margin: 10px 0 8px; }
  .welcome p { font-size: 10.5px; line-height: 15px; color: var(--text-muted); margin-bottom: 10px; }

  .collections { height: 333px; background: var(--section-grey); display: flex; justify-content: center; gap: 66px; padding-top: 16px; }
  .collection-card { width: 326px; text-align: center; }
  .collection-card h3 { font-family: "Oswald", sans-serif; font-weight: 500; font-size: 21px; color: var(--brand-red); margin-bottom: 4px; letter-spacing: 1px; line-height: 28px; }
  .collection-photo { height: 196px; }
  .collection-photo.marble {
    background:
      linear-gradient(180deg, #f6f6f4 0%, #e4e2de 45%, rgba(0,0,0,0) 46%),
      linear-gradient(160deg, #ffffff 0%, #d4d4d2 50%, #8f8f8f 100%);
  }
  .collection-photo.sculpture {
    background:
      radial-gradient(ellipse 90px 100px at 50% 50%, #b39a6c 0%, #6f5f45 55%, rgba(0,0,0,0) 100%),
      linear-gradient(180deg, #4a4238 0%, #2b251e 100%);
  }
  .collection-card p { font-size: 10px; line-height: 13px; color: var(--text-dark); margin: 8px 4px 8px; }
  .read-more { display: inline-block; background: var(--brand-red); color: var(--white); font-size: 8px; font-weight: 700; padding: 4px 10px; text-decoration: none; }

  .site-footer { height: 77px; background: var(--footer-dark); padding: 14px 60px 0; }
  .footer-row { display: flex; justify-content: space-between; align-items: center; height: 28px; border-bottom: 1px solid var(--footer-line); }
  .footer-nav a { color: #cfcfcf; font-size: 10px; text-decoration: none; padding: 0 14px; border-right: 1px solid #555; }
  .footer-nav a:last-child { border-right: none; }
  .social-links { display: flex; gap: 10px; }
  .social-links span { width: 18px; height: 18px; border-radius: 50%; background: #4a4a4a; }
  .copyright { color: #9a9a9a; font-size: 9px; margin-top: 8px; padding-left: 14px; }
</style>
</head>
<body>
  <header class="site-header">
    <div class="brand"><span class="brand-square"></span><span class="brand-name">PETRA GROVE</span></div>
    <div class="call-now">Call Now : <span class="phone">(555) 013 2748</span></div>
  </header>

  <nav class="main-nav">
    <a href="#">Home</a>
    <a href="#">Main Category Template</a>
    <a href="#">Sub Category Template</a>
    <a href="#">About us</a>
    <a href="#">Contact us</a>
  </nav>

  <section class="hero">
    <div class="hero-panel lounge" role="img" aria-label="Lounge with dark furniture and mosaic-tiled columns"></div>
    <div class="hero-panel fireplace" role="img" aria-label="Grey mosaic feature wall with a lit fireplace"></div>
    <div class="hero-panel bathroom" role="img" aria-label="Bright bathroom with mosaic-tiled walls and window"></div>
    <div class="hero-labels"><span>PUBLIC</span><span>COMMERCIAL</span><span>OVERSEAS</span></div>
  </section>

  <section class="welcome">
    <h1>WELCOME TO PETRA GROVE</h1>
    <h2>Sed ut perspiciatis unde omnis iste natus error sit voluptatem.</h2>
    <p>Lorem ipsum dolor sit amet, consectetur adipiscing elit, sed do eiusmod tempor incididunt ut labore et dolore magna aliqua. Ut enim ad minim veniam, quis nostrud exercitation ullamco laboris nisi ut aliquip ex ea commodo consequat. Duis aute irure dolor in reprehenderit in voluptate velit esse cillum dolore eu fugiat nulla pariatur. Excepteur sint occaecat cupidatat non proident, sunt in culpa qui officia deserunt mollit anim id est laborum.</p>
    <p>Sed ut perspiciatis unde omnis iste natus error sit voluptatem accusantium doloremque laudantium, totam rem aperiam, eaque ipsa quae ab illo inventore veritatis et quasi architecto beatae vitae dicta sunt explicabo. Nemo enim ipsam voluptatem quia voluptas sit aspernatur aut odit aut fugit, sed quia consequuntur magni dolores eos qui ratione voluptatem sequi nesciunt.</p>
  </section>

  <section class="collections">
    <article class="collection-card">
      <h3>MARBLE</h3>
      <div class="collection-photo marble" role="img" aria-label="Bathroom with black and white marble floor tiles and a white tub"></div>
      <p>Lorem ipsum dolor sit amet, consectetur adipiscing elit, sed do eiusmod tempor incididunt ut labore et dolore magna aliqua. Ut enim ad minim veniam, quis nostrud exercitation.</p>
      <a class="read-more" href="#">READ MORE</a>
    </article>
    <article class="collection-card">
      <h3>SCULPTURE</h3>
      <div class="collection-photo sculpture" role="img" aria-label="Carved bronze-toned stone sculpture on a dark background"></div>
      <p>Lorem ipsum dolor sit amet, consectetur adipiscing elit, sed do eiusmod tempor incididunt ut labore et dolore magna aliqua. Ut enim ad minim veniam, quis nostrud exercitation.</p>
      <a class="read-more" href="#">READ MORE</a>
    </article>
  </section>

  <footer class="site-footer">
    <div class="footer-row">
      <nav class="footer-nav">
        <a href="#">Home</a><a href="#">Main Category Template</a><a href="#">Sub Category Template</a><a href="#">About us</a><a href="#">Contact us</a>
      </nav>
      <div class="social-links" aria-label="Social links"><span></span><span></span><span></span><span></span><span></span><span></span></div>
    </div>
    <p class="copyright">Copyright © 2014 All Rights Reserved | Privacy Policy</p>
  </footer>
</body>
</html>
```